Construction Site Sign

4' high x 8' wide construction site sign using the attached logo (small correction required) Utilize the red, white and blue colors; add the company address, telephone numbers and website.

418 Pellham Creek Lane, Suite 3
Fenmoor, Westland 40718
(706) 555-0182 Office
(706) 555-0139 Fax
www.ridgelinebuilders.biz

Industry/Entity Type

Construction

```html
<!DOCTYPE html>
<html lang="en">
<head>
<meta charset="utf-8">
<title>Ridgeline Builders Inc – Site Sign</title>
<link rel="stylesheet" href="https://fonts.googleapis.com/css2?family=Arimo:wght@400;700&display=swap">
<style>
  :root {
    --backdrop: #7a716f;
    --sign-white: #ffffff;
    --flag-red: #e8232c;
    --flag-blue: #1359a7;
    --band-grey: #a6a9aa;
    --text-white: #ffffff;
  }
  html, body {
    margin: 0;
    padding: 0;
    width: 1200px;
    height: 720px;
    overflow: hidden;
    background: var(--backdrop);
    font-family: "Arimo", Arial, sans-serif;
  }
  .canvas {
    position: relative;
    width: 1200px;
    height: 720px;
  }
  .sign {
    position: absolute;
    left: 112px;
    top: 116px;
    width: 976px;
    height: 488px;
    background: var(--sign-white);
    overflow: hidden;
  }
  .sign-panels {
    position: absolute;
    inset: 0;
  }
  .brand-name {
    position: absolute;
    left: 40px;
    top: 192px;
    width: 500px;
    margin: 0;
    text-align: center;
    color: var(--flag-blue);
    font-weight: 700;
    font-size: 52px;
    line-height: 1.1;
    letter-spacing: 1px;
    text-transform: uppercase;
  }
  .contact-phones {
    position: absolute;
    right: 26px;
    top: 40px;
    margin: 0;
    padding: 0;
    list-style: none;
  }
  .contact-phones li {
    display: flex;
    align-items: center;
    justify-content: flex-end;
    height: 56px;
    color: var(--text-white);
    font-weight: 700;
    font-size: 41px;
    letter-spacing: 2px;
    word-spacing: 8px;
    white-space: nowrap;
  }
  .phone-badge {
    display: inline-flex;
    align-items: center;
    justify-content: center;
    width: 36px;
    height: 36px;
    margin-right: 12px;
    border-radius: 50%;
    background: var(--flag-red);
    border: 2px solid #f3c9cb;
    box-sizing: border-box;
    color: var(--text-white);
    font-size: 21px;
    font-weight: 700;
    letter-spacing: 0;
  }
  .address {
    position: absolute;
    right: 38px;
    top: 245px;
    margin: 0;
    font-style: normal;
    text-align: right;
    color: var(--text-white);
    font-weight: 400;
    font-size: 29px;
    line-height: 43px;
  }
  .web-band {
    position: absolute;
    left: 0;
    bottom: 0;
    width: 100%;
    height: 62px;
    background: var(--band-grey);
    display: flex;
    align-items: center;
    justify-content: center;
  }
  .web-address {
    margin-left: -20px;
    color: var(--text-white);
    font-weight: 700;
    font-size: 34px;
    letter-spacing: 0.5px;
  }
</style>
</head>
<body>
<div class="canvas">
  <section class="sign">
    <svg class="sign-panels" width="976" height="488" viewBox="0 0 976 488" aria-hidden="true">
      <polygon points="518,0 976,0 976,180 567,180" fill="var(--flag-red)"/>
      <polygon points="567,180 976,180 976,426 633,426" fill="var(--flag-blue)"/>
      <polygon points="500,0 507,0 556,180 549,180" fill="var(--flag-red)"/>
      <polygon points="549,180 556,180 623,426 616,426" fill="var(--flag-blue)"/>
    </svg>

    <h1 class="brand-name">Ridgeline<br>Builders Inc</h1>

    <ul class="contact-phones">
      <li><span class="phone-badge">P</span>(706) 555-0182</li>
      <li><span class="phone-badge">F</span>(706) 555-0139</li>
    </ul>

    <address class="address">
      418 Pellham Creek Lane,<br>
      Suite 3 Fenmoor,<br>
      Westland 40718
    </address>

    <div class="web-band">
      <span class="web-address">www.ridgelinebuilders.biz</span>
    </div>
  </section>
</div>
</body>
</html>
```